Book Cover

Hello!
I need someone to design a book cover with the title, subtitle and one of the photos attached.

- Title: Beyond the Grey Hours - By Corwin Ashdale
- Subtitle: A Steady Handbook for finding calm and strength after hard news.

```html
<!DOCTYPE html>
<html lang="en">
<head>
<meta charset="UTF-8">
<title>Beyond the Grey Hours — Book Cover</title>
<link rel="stylesheet" href="https://fonts.googleapis.com/css2?family=Allura&family=Anton&family=Bebas+Neue&family=Poppins:wght@500&display=swap">
<style>
  :root {
    --backdrop: #2b2b2d;
    --teal-top: #2e7b91;
    --teal-bottom: #226a7f;
    --gold: #e8ad1b;
    --gold-deep: #dc9f12;
    --gold-title: #ebb01d;
    --ink-light: #ececec;
    --portrait-a: #7a8497;
    --portrait-b: #2f4a8f;
  }
  * { margin: 0; padding: 0; box-sizing: border-box; }
  html, body { width: 1200px; height: 1200px; overflow: hidden; }
  body {
    background: var(--backdrop);
    position: relative;
  }
  .cover {
    position: absolute;
    left: 173px;
    top: 0;
    width: 854px;
    height: 1200px;
    overflow: hidden;
    background: linear-gradient(180deg, var(--teal-top) 0%, var(--teal-bottom) 55%);
  }
  .cover__ground {
    position: absolute;
    left: 0;
    top: 580px;
    width: 854px;
    height: 620px;
  }
  .cover__author {
    position: absolute;
    top: 62px;
    left: 0;
    width: 100%;
    text-align: center;
    padding-right: 40px;
    font-family: "Allura", cursive;
    font-size: 50px;
    color: var(--ink-light);
    line-height: 1;
  }
  .cover__title-lead {
    position: absolute;
    top: 160px;
    left: 0;
    width: 100%;
    text-align: center;
    font-family: "Poppins", sans-serif;
    font-weight: 500;
    font-size: 92px;
    line-height: 1;
    color: var(--ink-light);
    letter-spacing: -1px;
    text-shadow: 0 3px 6px rgba(0,0,0,0.25);
  }
  .cover__title-main {
    position: absolute;
    top: 268px;
    left: 0;
    width: 100%;
    text-align: center;
    font-family: "Anton", sans-serif;
    font-size: 138px;
    line-height: 1;
    color: var(--gold-title);
    letter-spacing: 2px;
    -webkit-text-stroke: 1.5px rgba(255,255,255,0.55);
    text-shadow: 0 4px 8px rgba(0,0,0,0.35);
  }
  .cover__subtitle {
    position: absolute;
    top: 412px;
    left: 0;
    width: 100%;
    text-align: center;
    font-family: "Bebas Neue", sans-serif;
    font-size: 41px;
    line-height: 1.12;
    letter-spacing: 1px;
    color: var(--ink-light);
    text-shadow: 0 2px 4px rgba(0,0,0,0.3);
  }
  .cover__portrait {
    position: absolute;
    left: 58px;
    top: 508px;
    width: 712px;
    height: 692px;
    border-radius: 240px 240px 0 0;
    background: radial-gradient(ellipse at 50% 20%, var(--portrait-a) 0%, var(--portrait-b) 70%);
  }
</style>
</head>
<body>
  <main class="cover">
    <svg class="cover__ground" viewBox="0 0 854 620" preserveAspectRatio="none" aria-hidden="true">
      <defs>
        <linearGradient id="groundFill" x1="0" y1="0" x2="0" y2="1">
          <stop offset="0" stop-color="var(--gold)"/>
          <stop offset="1" stop-color="var(--gold-deep)"/>
        </linearGradient>
      </defs>
      <path fill="url(#groundFill)" d="M0 74 L40 66 L70 72 L110 60 L150 64 L190 56 L225 62 L255 40 L300 30 L330 14 L360 22 L395 18 L430 26 L470 20 L505 34 L540 30 L575 44 L610 40 L650 52 L690 48 L730 56 L770 50 L800 40 L830 30 L854 18 L854 620 L0 620 Z"/>
    </svg>

    <p class="cover__author">Corwin Ashdale</p>
    <h1 class="cover__title">
      <span class="cover__title-lead">Beyond the</span>
      <span class="cover__title-main">GREY HOURS</span>
    </h1>
    <p class="cover__subtitle">A Steady Handbook for finding calm and<br>strength after hard news.</p>

    <div class="cover__portrait" role="img" aria-label="Portrait of the author, an older man in a blue jacket looking upward"></div>
  </main>
</body>
</html>
```